3 in 1 website - Home Lens Studio Extra + Keeping Moments LLC + Marla's Game Shots

Help me simplify and organize my business life. I am a sports photographer (action, individual and teams), real estate photographer (stills and drones) and I transfer videos and photos to jump drives, along with photo restoration, etc. Currently, I have a functioning website for the transfer/restoration business at KeepingMomentsLLC.example which was recently created and I like it. I have received several really good ideas for the Real Estate Photography portion! I don't have anything started for the Sports Pics. My vision possibly includes a main/home page giving people the option to choose real estate, sports or transfer/restoration. I just want them combined into one site....somehow to better organize my businesses and give me ONE place to keep to updated and check for communication. I just updated the brief again and added logo files for my "parent" company called "Keeping Moments". I prefer this logo at the top of the main/home page, please. I previously uploaded the logo for Home Lens Studio Extra which would be used with the real estate portion of my business. At this point, I don't have a logo for the sports photography portion.

Target Market(s)

Real Estate Agents and Brokers; Sports team, parents and boosters; Community members typically 40+ years old

Industry/Entity Type

Real Estate Photography; Local sports teams; Community members 40+ years old

Coding

Coded - Design and coding required

Number of Pages Required

3 page

Requirements
Must have
• At least one page for each area: real estate, sports, digital transfers. The real estate will need to connect to an account I have with QNL for checkout options. The sports page(s) will need to connect to a 3rd party service, also. The digital transfers, photo restorations, etc. would just need a way for them to request service.
Nice to have
• I currently have a website at KeepingMomentsLLC.example for the digital transfer/photo restoration part of my business. I like this website but want it integrated with one main site for all 3 businesses.

```html
<!DOCTYPE html>
<html lang="en">
<head>
<meta charset="utf-8">
<title>Marla Whitcombe — Photography</title>
<link rel="stylesheet" href="https://fonts.googleapis.com/css2?family=Lato:wght@400;700;900&family=Comfortaa:wght@600;700&family=Dancing+Script:wght@500&display=swap">
<style>
:root{
  --teal:#15948f;
  --teal-dark:#0f7471;
  --red:#e8262a;
  --orange:#ef4623;
  --blue:#1f5fa8;
  --ink:#1d1d1d;
  --text:#3b3b3b;
  --grey:#f0f0f0;
  --panel:#eaf4f8;
  --stage:#2f2f2f;
  --black:#000;
}
*{box-sizing:border-box;margin:0;padding:0}
html,body{width:1200px;height:2267px;overflow:hidden}
body{background:var(--stage);font-family:"Lato",sans-serif;color:var(--text);position:relative}
.page{position:absolute;width:537px;background:#fff;overflow:hidden}
.page--home{left:42px;top:37px;height:1704px}
.page--estate{left:620px;top:33px;height:2191px}
.abs{position:absolute}
.topbar{position:absolute;top:0;right:0;height:24px;background:var(--teal);color:#fff;font-size:6.5px;display:flex;align-items:center;gap:14px;padding-left:26px;padding-right:40px;clip-path:polygon(14px 0,100% 0,100% 100%,0 100%)}
.topbar span{display:flex;align-items:center;gap:4px}
.topbar svg{width:8px;height:8px;fill:#fff}
.nav{position:absolute;top:36px;display:flex;align-items:center;gap:15px;font-size:6.5px;color:var(--ink);font-weight:700}
.nav .active{color:var(--orange);text-decoration:underline}
.page--estate .nav .active{color:var(--red)}
.btn{display:inline-block;color:#fff;font-weight:700;text-align:center;transform:skewX(-12deg);font-size:6.5px;letter-spacing:.2px}
.btn b{display:inline-block;transform:skewX(12deg);font-weight:700}
.btn--teal{background:var(--teal)}
.btn--red{background:var(--red)}
.btn--orange{background:var(--orange)}
.brand{position:absolute;display:flex;align-items:center;gap:5px;font-family:"Comfortaa",sans-serif;font-weight:700}
.brand i{display:block;border-radius:50%}
.photo{position:absolute}
.hero{position:absolute;left:0;width:537px}
.script{font-family:"Dancing Script",cursive;font-weight:500}
.display{font-family:"Comfortaa",sans-serif;font-weight:700;color:var(--ink)}
.p{font-size:6.3px;line-height:1.75}
.sec-title{font-weight:900;font-size:14px;line-height:1.2;color:var(--ink);text-transform:uppercase}
.sec-title em{font-style:normal;color:var(--red);display:block}
.frame{position:absolute;border:2px solid var(--teal)}
.dot{position:absolute;width:4px;height:4px;border-radius:50%;background:#fff}
.sq{position:absolute}
.c-item{position:absolute;display:flex;gap:10px;align-items:flex-start}
.c-icon{width:28px;height:28px;border-radius:50%;background:var(--teal);display:flex;align-items:center;justify-content:center;flex:none}
.c-icon svg{width:11px;height:11px;fill:#fff}
.c-item h4{font-size:7.5px;color:var(--ink);font-weight:700;margin-top:2px}
.c-item p{font-size:7px;line-height:1.5;color:#555}
.form{position:absolute;background:var(--panel);padding:18px 12px}
.field{background:#fff;border:1px solid #e3e3e3;font-size:6.5px;color:#555;padding:0 8px;height:22px;display:flex;align-items:center}
.row{display:flex;gap:5px;margin-bottom:6px}
.row .field{flex:1}
.msg{height:50px;align-items:flex-start;padding-top:7px;margin-bottom:12px}
.dots{position:absolute;width:24px;height:40px;background-image:radial-gradient(var(--teal) 0.8px,transparent 1px);background-size:4px 4px}
.footer{position:absolute;left:0;width:537px;background:var(--black);color:#fff}
.f-nav{position:absolute;display:flex;gap:12px;font-size:6px}
.f-line{position:absolute;font-size:5.5px}
.socials{position:absolute;display:flex;gap:9px}
.socials i{display:block;width:10px;height:10px;border-radius:50%;background:var(--teal)}
.f-bar{position:absolute;left:0;bottom:0;width:100%;height:3px;background:var(--teal)}
.pkg{position:absolute;background:#fff;box-shadow:0 2px 6px rgba(0,0,0,.15);padding-bottom:10px}
.pkg-head{background:var(--teal);color:#fff;font-weight:900;text-transform:uppercase;text-align:center;position:relative}
.pkg--vip .pkg-head{background:var(--red)}
.price{position:absolute;left:50%;transform:translateX(-50%);border-radius:50%;background:#fff;border:3px solid var(--teal);color:var(--teal);font-weight:900;display:flex;align-items:center;justify-content:center}
.pkg--vip .price,.addon--red .price{border-color:var(--red);color:var(--red)}
.ticks{list-style:none;color:var(--text)}
.ticks li{position:relative;padding-left:13px}
.ticks li::before{content:"";position:absolute;left:2px;top:1px;width:3px;height:5px;border:solid var(--red);border-width:0 1.3px 1.3px 0;transform:rotate(45deg)}
.pkg--vip .ticks li::before{border-color:var(--teal)}
.addon{position:absolute;background:#fff;box-shadow:0 2px 6px rgba(0,0,0,.14);padding-bottom:10px}
.addon .pkg-head{font-size:8.5px;padding:0 8px;display:flex;align-items:center;justify-content:center;line-height:1.3}
.addon--red .pkg-head{background:var(--red)}
.addon .price{width:44px;height:44px;font-size:13px}
.addon .body{font-size:6.2px;line-height:1.7;padding:0 8px}
.rates{list-style:none;font-size:6.5px;padding:0 8px}
.rates li{display:flex;padding-left:16px;position:relative;margin-bottom:9px}
.rates li::before{content:"";position:absolute;left:3px;top:0;width:3px;height:5px;border:solid var(--red);border-width:0 1.3px 1.3px 0;transform:rotate(45deg)}
.rates b{margin-left:auto;margin-right:24px;color:var(--red)}
</style>
</head>
<body>

<main class="page page--home">
  <header>
    <div class="brand" style="left:49px;top:16px;color:var(--teal);font-size:12px;flex-direction:column;align-items:flex-start;gap:2px">
      <span style="display:flex;align-items:center;gap:5px"><i style="width:12px;height:12px;background:var(--teal)"></i>Marla Whitcombe</span>
      <span style="font-size:4.5px;letter-spacing:2px;padding-left:36px">PHOTOGRAPHER</span>
    </div>
    <div class="topbar" style="width:324px">
      <span><svg viewBox="0 0 10 10"><path d="M2 0l2 2-1 1.5c.6 1.3 2 2.7 3.5 3.5L8 6l2 2-1.5 2C4 10 0 6 0 1.5z"/></svg>Call: 1-555-010-0195</span>
      <span><svg viewBox="0 0 10 10"><path d="M0 2h10v6H0zM0 2l5 3.5L10 2" stroke="#15948f" stroke-width=".8"/></svg>Mail: info@marlawhitcombe.example</span>
      <span><svg viewBox="0 0 10 10"><path d="M0 1h2l1.5 5h5L10 2.5H3"/><circle cx="4" cy="8.5" r="1"/><circle cx="8" cy="8.5" r="1"/></svg></span>
    </div>
    <nav class="nav" style="left:198px">
      <span class="active">Home</span><span>About Us</span><span>Real Estate</span><span>Sports</span><span>Keeping Moments</span>
      <span class="btn btn--teal" style="width:52px;line-height:17px;margin-left:4px"><b>Contact Us</b></span>
    </nav>
  </header>

  <section class="hero" style="top:55px;height:259px;background:linear-gradient(120deg,#1f7d89,#17707e 60%,#1c8792)">
    <div class="script abs" style="left:46px;top:54px;color:#fff;font-size:15px">Welcome to</div>
    <h1 class="display abs" style="left:46px;top:76px;color:#fff;font-size:21px">Marla Whitcombe</h1>
    <div class="abs" style="left:46px;top:110px;color:#fff;font-size:6px;letter-spacing:1.8px;font-weight:700">PHOTOGRAPHER</div>
    <p class="p abs" style="left:46px;top:119px;width:222px;color:#fff">Welcome to my website and look forward to working with you soon! My nameis Marla Whitcombe and after working in the field of education for over 21 yearsand being a part-time photographer.</p>
    <span class="btn btn--orange abs" style="left:49px;top:165px;width:113px;line-height:24px;font-size:7px"><b>Schedule Appointments</b></span>
    <div class="photo" style="left:302px;top:38px;width:176px;height:132px;background:var(--orange);transform:rotate(3deg)"></div>
    <div class="photo" role="img" aria-label="Photographer shooting a bright modern kitchen interior" style="left:295px;top:31px;width:176px;height:132px;border:3px solid #fff;background:linear-gradient(135deg,#e9e2d6,#b79a78 45%,#2c3140 80%);transform:rotate(3deg)"></div>
    <div class="sq" style="left:507px;top:177px;width:30px;height:30px;background:#cde8ea"></div>
    <div class="sq" style="left:481px;top:207px;width:30px;height:30px;background:#b5dadd"></div>
    <div class="sq" style="left:449px;top:223px;width:36px;height:36px;background:#dcefef"></div>
    <div class="sq" style="left:405px;top:232px;width:44px;height:27px;background:#c1e1e3"></div>
    <div class="dot" style="left:258px;top:234px"></div>
    <div class="dot" style="left:268px;top:234px;background:var(--orange)"></div>
    <div class="dot" style="left:278px;top:234px"></div>
  </section>

  <section class="abs" style="top:314px;left:0;width:537px;height:235px">
    <div class="abs" role="img" aria-label="Row of suburban houses at sunset" style="left:0;top:70px;width:537px;height:165px;background:linear-gradient(180deg,rgba(255,255,255,1) 0%,rgba(238,226,214,.7) 40%,#c2a48e 70%,#8c6f61 100%)"></div>
    <div class="script abs" style="left:0;width:537px;text-align:center;top:50px;color:var(--teal);font-size:11px">About</div>
    <h2 class="display abs" style="left:0;width:537px;text-align:center;top:63px;font-size:16px">Marla Whitcombe</h2>
    <p class="p abs" style="left:68px;width:400px;top:87px;text-align:center;color:#222">Welcome to my website and look forward to working with you soon! My nameis Marla Whitcombe and after working in the field of education for over 21 yearsand being a part-time photographer, I made the move in December 2021 to be afull-time photographer and do what I love! I am married to Sam Whitcombe, anexcellent veterinarian at Larkfield Pet Care Clinic in Fairview.</p>
    <p class="p abs" style="left:68px;width:400px;top:140px;text-align:center;color:#222">We recentlycelebrated our 36 th anniversary. We have two adult children, JT Whitcombe andHannah Whitcombe. JT is an RN in ICU at Oakmere Valley Hospital and Hannah is a caregiver forKindwell Care Partners. We are extremely proud of both our children!</p>
    <span class="btn btn--teal abs" style="left:236px;top:168px;width:64px;line-height:17px"><b>READ MORE</b></span>
  </section>

  <section class="abs" style="top:549px;left:0;width:537px;height:215px;background:var(--grey)">
    <h2 class="sec-title abs" style="left:50px;top:72px"><em>Real</em>Estate Photography</h2>
    <p class="p abs" style="left:50px;top:113px;width:200px">During the later part of 2022, I began taking classes and studying the besttechniques for taking quality real estate photos for realtors.<br>Thus is January2023, I added Home Lens Studio Extra! I am absolutely loving this new addition to my services!!</p>
    <span class="btn btn--teal abs" style="left:53px;top:175px;width:65px;line-height:19px"><b>LEARN MORE</b></span>
    <div class="photo" role="img" aria-label="Hands holding printed interior photos beside a laptop" style="left:283px;top:30px;width:254px;height:185px;background:linear-gradient(135deg,#efefef,#d9d6d2 45%,#a9a39a 75%,#6f6a64)"></div>
    <div class="frame" style="left:268px;top:15px;width:251px;height:182px"></div>
  </section>

  <section class="abs" style="top:764px;left:0;width:537px;height:264px">
    <div class="photo" role="img" aria-label="Sports photographer with a long telephoto lens at a football game" style="left:0;top:47px;width:252px;height:184px;background:linear-gradient(135deg,#5f89c3,#4a6b55 40%,#c7754f 70%,#7a4632)"></div>
    <div class="frame" style="left:16px;top:31px;width:251px;height:183px;border-color:var(--blue)"></div>
    <h2 class="sec-title abs" style="left:288px;top:80px"><em>Sports</em>Photography</h2>
    <p class="p abs" style="left:288px;top:118px;width:200px">I began taking action sports pictures almost 20 years ago, first as a parent then Ihad the opportunity to join the team at www.FieldLightFrames.example at itsinception in July 2017.</p>
    <p class="p abs" style="left:288px;top:160px;width:200px">I absolutely love taking action sports shots and seeing the dedication in the expressions of athletes.</p>
    <span class="btn btn--teal abs" style="left:290px;top:198px;width:65px;line-height:19px"><b>LEARN MORE</b></span>
  </section>

  <section class="abs" style="top:1028px;left:0;width:537px;height:215px;background:var(--grey)">
    <h2 class="sec-title abs" style="left:50px;top:52px"><em>Keeping</em>Moments</h2>
    <p class="p abs" style="left:50px;top:90px;width:205px">In January 2022, I opened my office at 240 North Maple Street, Fairview, KY40001. It is in a great historic building with lots of personality and architecture.</p>
    <p class="p abs" style="left:50px;top:133px;width:205px">When I first opened it, I worked with individuals who had boxes &amp; boxes of oldfamily photos, but no idea what was really in the boxes.</p>
    <span class="btn btn--teal abs" style="left:53px;top:165px;width:65px;line-height:19px"><b>LEARN MORE</b></span>
    <div class="photo" role="img" aria-label="Vintage folding camera resting on old family photographs" style="left:283px;top:30px;width:254px;height:185px;background:linear-gradient(135deg,#e9e9e9,#9a9a9a 45%,#3a3a3a 75%,#bdbdbd)"></div>
    <div class="frame" style="left:268px;top:14px;width:251px;height:184px"></div>
  </section>

  <section class="abs" style="top:1243px;left:0;width:537px;height:298px;background:linear-gradient(160deg,#fff,#f6f6f6)">
    <div class="script abs" style="left:0;width:537px;text-align:center;top:40px;color:var(--teal);font-size:11px">Contact Us</div>
    <h2 class="display abs" style="left:0;width:537px;text-align:center;top:54px;font-size:16px">Get In Touch With Us</h2>
    <div class="abs" style="left:49px;top:92px;font-size:11px;font-weight:700;color:var(--ink)">Address</div>
    <div class="c-item" style="left:49px;top:113px"><div class="c-icon"><svg viewBox="0 0 10 10"><path d="M5 0a3.5 3.5 0 0 0-3.5 3.5C1.5 6 5 10 5 10s3.5-4 3.5-6.5A3.5 3.5 0 0 0 5 0zm0 5a1.4 1.4 0 1 1 0-2.8A1.4 1.4 0 0 1 5 5z"/></svg></div><div><h4>LOCATION</h4><p>240 North Maple Street,<br>Fairview, KY 40001</p></div></div>
    <div class="c-item" style="left:49px;top:157px"><div class="c-icon"><svg viewBox="0 0 10 10"><path d="M2 0l2 2-1 1.5c.6 1.3 2 2.7 3.5 3.5L8 6l2 2-1.5 2C4 10 0 6 0 1.5z"/></svg></div><div><h4>PHONE NUMBER</h4><p>1-555-010-0195</p></div></div>
    <div class="c-item" style="left:49px;top:201px"><div class="c-icon"><svg viewBox="0 0 10 10"><path d="M0 2h10v6H0z"/><path d="M0 2l5 3.5L10 2" stroke="#15948f" stroke-width=".8" fill="none"/></svg></div><div><h4>EMAIL ADDRESS</h4><p>info@marlawhitcombe.example</p></div></div>
    <div class="form" style="left:246px;top:84px;width:239px;height:176px">
      <div class="row"><div class="field">First Name</div><div class="field">Your Email</div></div>
      <div class="row"><div class="field">Your Phone</div><div class="field">Address</div></div>
      <div class="field msg">Message</div>
      <span class="btn btn--teal" style="width:62px;line-height:19px;margin-left:3px"><b>SUBMIT</b></span>
    </div>
    <div class="dots" style="left:462px;top:230px"></div>
  </section>

  <footer class="footer" style="top:1541px;height:163px">
    <div class="sq" style="left:0;top:60px;width:30px;height:60px;background:#555"></div>
    <div class="sq" style="left:30px;top:60px;width:30px;height:30px;background:#7a7a7a"></div>
    <div class="sq" style="left:60px;top:30px;width:30px;height:30px;background:#9a9a9a"></div>
    <div class="sq" style="left:90px;top:30px;width:30px;height:30px;background:#bdbdbd"></div>
    <div class="sq" style="left:120px;top:0;width:30px;height:30px;background:#cfcfcf"></div>
    <div class="sq" style="left:150px;top:0;width:30px;height:30px;background:#9a9a9a"></div>
    <div class="sq" style="left:0;top:90px;width:30px;height:30px;background:#8c8c8c"></div>
    <div class="sq" style="left:30px;top:30px;width:30px;height:30px;background:#d8d8d8"></div>
    <div class="brand" style="left:64px;top:98px;color:#fff;font-size:11px"><i style="width:11px;height:11px;background:#fff"></i>Marla Whitcombe</div>
    <nav class="f-nav" style="left:217px;top:74px"><span>HOME</span><span>ABOUT</span><span>REAL ESTATE</span><span>SPORTS</span><span>KEEPING MOMENTS</span><span>CONTACT US</span></nav>
    <div class="f-line" style="left:217px;top:90px">Phone : 1-555-010-0195 &nbsp;&nbsp; | &nbsp;&nbsp; Email : info@marlawhitcombe.example</div>
    <div class="f-line" style="left:217px;top:109px">Copyrights@2023.Marla Whitcombe Photographer.All Rights Reserved</div>
    <div class="socials" style="left:217px;top:124px"><i></i><i></i><i></i><i></i></div>
    <div class="f-bar"></div>
  </footer>
</main>

<main class="page page--estate">
  <header>
    <div class="brand" style="left:49px;top:14px;flex-direction:column;align-items:flex-start;gap:3px">
      <span style="display:flex;align-items:center;gap:5px;color:var(--red);font-size:11px"><i style="width:10px;height:10px;background:var(--red);border-radius:0"></i>Marla Whitcombe</span>
      <span style="font-family:Lato,sans-serif;font-size:6.5px;color:var(--teal);font-weight:700;padding-left:15px">Real Estate Photographer</span>
    </div>
    <div class="topbar" style="width:316px">
      <span><svg viewBox="0 0 10 10"><path d="M2 0l2 2-1 1.5c.6 1.3 2 2.7 3.5 3.5L8 6l2 2-1.5 2C4 10 0 6 0 1.5z"/></svg>Call:+1 555 010 8888</span>
      <span><svg viewBox="0 0 10 10"><path d="M0 2h10v6H0z"/></svg>Mail: info@marlawhitcombe.example</span>
      <span><svg viewBox="0 0 10 10"><path d="M0 1h2l1.5 5h5L10 2.5H3"/><circle cx="4" cy="8.5" r="1"/><circle cx="8" cy="8.5" r="1"/></svg></span>
    </div>
    <nav class="nav" style="left:198px;gap:13px;font-size:6.3px">
      <span>HOME</span><span>ABOUT US</span><span class="active">REAL ESTATE</span><span>SPORTS</span><span>DIGITAL TRANSFERS</span>
      <span class="btn btn--teal" style="width:52px;line-height:17px;margin-left:4px"><b>CONTACT US</b></span>
    </nav>
  </header>

  <section class="hero" style="top:55px;height:263px;background:linear-gradient(125deg,#1f8c86,#1a7d79 55%,#259b93)">
    <div class="abs" style="left:49px;top:42px;color:#fff;font-size:11px;font-weight:700">WELCOME TO</div>
    <h1 class="abs" style="left:49px;top:58px;color:#fff;font-size:18px;font-weight:700;line-height:1.25">HOME LENS STUDIO<br>EXTRA</h1>
    <p class="p abs" style="left:49px;top:105px;width:220px;color:#fff">Itaque earum rerum hic tenetur a sapiente delectus, ut aut reiciendis voluptatibus ut perferendis doloribus asperiores repellat.</p>
    <span class="btn btn--red abs" style="left:52px;top:134px;width:111px;line-height:24px"><b>SCHEDULE APPOINTMENTS</b></span>
    <div class="photo" style="left:311px;top:40px;width:165px;height:116px;background:var(--red);transform:rotate(3deg)"></div>
    <div class="photo" role="img" aria-label="Living room with leather sofas and dining table" style="left:305px;top:34px;width:165px;height:116px;border:3px solid #fff;background:linear-gradient(135deg,#d9d3c9,#8a7766 45%,#4c3f36 80%);transform:rotate(3deg)"></div>
    <div class="dot" style="left:258px;top:210px"></div>
    <div class="dot" style="left:268px;top:210px;background:var(--red)"></div>
    <div class="dot" style="left:278px;top:210px"></div>
    <svg class="abs" style="left:0;top:200px" width="537" height="64" viewBox="0 0 537 64">
      <polygon points="0,33 268,6 537,33 537,64 0,64" fill="var(--red)"/>
      <polygon points="0,45 268,18 537,45 537,64 0,64" fill="#fff"/>
    </svg>
  </section>

  <section class="abs" style="top:318px;left:0;width:537px;height:480px">
    <h2 class="abs" style="left:0;width:537px;top:49px;text-align:center;font-size:13px;font-weight:900;color:var(--ink);line-height:1.35"><span style="color:var(--red)">OUR</span><br>PACKAGES</h2>

    <div class="pkg" style="left:27px;top:135px;width:110px">
      <div class="pkg-head" style="height:53px;font-size:7px;padding-top:12px">The Ultimate Package</div>
      <div class="price" style="top:28px;width:46px;height:46px;font-size:12px">$150</div>
      <ul class="ticks" style="font-size:5.6px;line-height:1.5;padding:30px 4px 0 5px">
        <li style="margin-bottom:4px">Up to 25 BrightTrue+ Still Images</li><li style="margin-bottom:4px">Branded &amp; Non-Branded Property Website Links</li><li style="margin-bottom:4px">Company Branding</li><li style="margin-bottom:4px">Agent photo &amp; contact information</li><li style="margin-bottom:4px">Link to agent Property Website gallery</li><li style="margin-bottom:4px">Property description &amp; details</li><li style="margin-bottom:4px">Weekly Seller's report</li><li style="margin-bottom:4px">Posting to MLS</li><li style="margin-bottom:4px">High resolution printable still photos</li><li style="margin-bottom:4px">Unlimited text updates</li><li>Music enabled</li>
      </ul>
    </div>

    <div class="pkg pkg--vip" style="left:136px;top:89px;width:157px;z-index:2">
      <div class="pkg-head" style="height:68px;font-size:10px;padding-top:15px">The VIP Package</div>
      <div class="price" style="top:40px;width:52px;height:52px;font-size:14px">$200</div>
      <ul class="ticks" style="font-size:6.8px;line-height:1.5;padding:33px 6px 0 7px">
        <li style="margin-bottom:7px">Up to 50 BrightTrue+ Still Images</li><li style="margin-bottom:7px">Branded &amp; Non-Branded Property Website Links</li><li style="margin-bottom:7px">Company Branding</li><li style="margin-bottom:7px">Agent photo &amp; contact information</li><li style="margin-bottom:7px">Link to agent Property Website gallery</li><li style="margin-bottom:7px">Property description &amp; details</li><li style="margin-bottom:7px">Weekly Seller's report</li><li style="margin-bottom:7px">Posting to MLS</li><li style="margin-bottom:7px">High resolution printable still photos</li><li style="margin-bottom:7px">Property description &amp; details</li><li style="margin-bottom:7px">Unlimited text updates</li><li>Music enabled</li>
      </ul>
    </div>

    <div class="pkg" style="left:292px;top:135px;width:113px">
      <div class="pkg-head" style="height:53px;font-size:7px;padding-top:9px;line-height:1.4">Aerial Drone Package<br>#1</div>
      <div class="price" style="top:30px;width:44px;height:44px;font-size:12px">$175</div>
      <ul class="ticks" style="font-size:5.6px;line-height:1.5;padding:27px 4px 0 5px">
        <li style="margin-bottom:4px">Up to 30 seconds of Aerial Drone Video &amp; Up to 6 Aerial Still Images</li><li style="margin-bottom:4px">Branded &amp; Non-Branded Property Website Links</li><li style="margin-bottom:4px">Company Branding</li><li style="margin-bottom:4px">Agent photo &amp; contact information</li><li style="margin-bottom:4px">Link to agent Property Website gallery</li><li style="margin-bottom:4px">Property description &amp; details</li><li style="margin-bottom:4px">Weekly Seller's report</li><li style="margin-bottom:4px">Posting to MLS</li><li style="margin-bottom:4px">High resolution printable still photos</li><li style="margin-bottom:4px">Unlimited text updates</li><li>Music enabled</li>
      </ul>
    </div>

    <div class="pkg" style="left:404px;top:135px;width:106px">
      <div class="pkg-head" style="height:53px;font-size:7px;padding-top:9px;line-height:1.4">Aerial Drone Package<br>#2</div>
      <div class="price" style="top:28px;width:42px;height:42px;font-size:12px">$225</div>
      <ul class="ticks" style="font-size:5.6px;line-height:1.5;padding:22px 4px 0 5px">
        <li style="margin-bottom:4px">Up to 3 minutes of Aerial Drone Video AND Up to 20 Aerial Still Images</li><li style="margin-bottom:4px">Branded &amp; Non-Branded Property Website Links</li><li style="margin-bottom:4px">Company Branding</li><li style="margin-bottom:4px">Agent photo &amp; contact information</li><li style="margin-bottom:4px">Link to agent Property Website gallery</li><li style="margin-bottom:4px">Property description &amp; details</li><li style="margin-bottom:4px">Weekly Seller's report</li><li style="margin-bottom:4px">Posting to MLS</li><li style="margin-bottom:4px">High resolution printable still photos</li><li style="margin-bottom:4px">Unlimited text updates</li><li>Music enabled</li>
      </ul>
    </div>

    <span class="btn btn--red abs" style="left:233px;top:454px;width:70px;line-height:22px"><b>ADD-ONS</b></span>
  </section>

  <section class="abs" style="top:820px;left:0;width:537px;height:900px">
    <div class="addon" style="left:46px;top:0;width:137px;min-height:145px">
      <div class="pkg-head" style="height:58px;padding-bottom:18px">NEW CONSTRUCTION PROGRESS SHOOT</div>
      <div class="price" style="top:36px">$95</div>
      <p class="body" style="margin-top:50px">Exterior and Interior HDR photography to market your new construction property before completion.</p>
    </div>
    <div class="addon" style="left:46px;top:150px;width:137px;min-height:233px">
      <div class="pkg-head" style="height:56px;padding-bottom:18px">INTERACTIVE FLOOR PLAN</div>
      <div class="price" style="top:34px">$125</div>
      <p class="body" style="margin-top:52px;color:#222">Choose a package based on the square footage of your home when you place your order, and we'll get started right away on your unique floor plan enabled virtual tour experience!</p>
      <ul class="rates" style="margin-top:10px"><li>Up to 3000 sq ft<b>$125</b></li><li>3001 to 4000 sq ft<b>$160</b></li><li>4001 to 5000 sq ft<b>$200</b></li><li>5001 to 6000 sq ft<b>$240</b></li></ul>
    </div>
    <div class="addon" style="left:46px;top:395px;width:137px;min-height:126px">
      <div class="pkg-head" style="height:56px;padding-bottom:18px">BRIGHTTRUE+ STILL IMAGES</div>
      <div class="price" style="top:34px">$5</div>
      <p class="body" style="margin-top:50px">Additional BrightTrue+ Still Images to share with your clients.</p>
    </div>
    <div class="addon" style="left:46px;top:544px;width:137px;min-height:126px">
      <div class="pkg-head" style="height:56px;padding-bottom:18px">VIRTUAL STAGING –<br>STILL IMAGE</div>
      <div class="price" style="top:34px">$30</div>
      <p class="body" style="margin-top:50px">Let us make sure your vacant property comes to life with virtual staging!</p>
    </div>
    <div class="addon" style="left:46px;top:695px;width:137px;min-height:183px">
      <div class="pkg-head" style="height:56px;padding-bottom:18px">TWILIGHT SESSION</div>
      <div class="price" style="top:34px">$75</div>
      <p class="body" style="margin-top:48px">Twilight and sunset images truly make a listing stand out!<br>Homes look better in the evening and have a warming glow to them.</p>
      <p class="body" style="margin-top:6px">You will simply love the magical and enchanting effect of our evening lens and you'll also have a gift for the seller.</p>
    </div>

    <div class="addon addon--red" style="left:190px;top:0;width:157px;min-height:136px">
      <div class="pkg-head" style="height:60px;padding-bottom:18px;font-size:9.5px">SHORT AERIAL DRONE</div>
      <div class="price" style="top:38px;width:48px;height:48px;font-size:14px">$150</div>
      <p class="body" style="margin-top:54px">Up to 1 minute of Aerial Drone Video &amp; Up to 6 Aerial Still Images</p>
    </div>
    <div class="addon addon--red" style="left:190px;top:151px;width:157px;min-height:142px">
      <div class="pkg-head" style="height:60px;padding-bottom:18px;font-size:9.5px">LONG AERIAL DRONE</div>
      <div class="price" style="top:38px;width:48px;height:48px;font-size:14px">$175</div>
      <p class="body" style="margin-top:54px">Up to 3 minutes of Aerial Drone Video &amp; Up to 20 Aerial Still Images</p>
    </div>
    <div class="addon addon--red" style="left:190px;top:302px;width:157px;min-height:231px">
      <div class="pkg-head" style="height:60px;padding-bottom:18px;font-size:9.5px">SINGLE PROPERTY WEBSITE</div>
      <div class="price" style="top:38px;width:48px;height:48px;font-size:14px">$25</div>
      <p class="body" style="margin-top:52px;color:#222">You are sure to impress your clients with this marketing tool!<br>Home shoppers will love you for it after a day of scouting when they turn to their computers for a closer look. Best of all its a mini site for you, and the home!</p>
      <p class="body" style="margin-top:7px;color:#222">A fee of $25 is billed annually for renewal until website and domain are no longer needed.</p>
    </div>
    <div class="addon addon--red" style="left:190px;top:545px;width:157px;min-height:297px">
      <div class="pkg-head" style="height:60px;padding-bottom:18px;font-size:9.5px">SOCIAL MEDIA VIDEO FILE</div>
      <div class="price" style="top:38px;width:48px;height:48px;font-size:14px">$20</div>
      <p class="body" style="margin-top:52px;color:#222">Stand-alone Social Media file with any of your virtual tour orders!<br>After completion of your drone and/or photography shoot, we will create a shorter (1-3 minutes) version of your production that will be given to you in a .MP4 format for you to upload to your social sites like Porchfeed and Reelharbor. The video will prominently display you picture and contact information throughout the entire production.</p>
      <p class="body" style="margin-top:7px;color:#222">If you would like us to create an even shorter version of the video for sites like Pinlark or Brieflet, just let us know and we'll make sure it's 30 seconds or less!</p>
    </div>

    <div class="addon" style="left:355px;top:0;width:137px;min-height:128px">
      <div class="pkg-head" style="height:56px;padding-bottom:18px">EXTERIOR ONLY</div>
      <div class="price" style="top:34px">$95</div>
      <p class="body" style="margin-top:52px">We capture only the exterior of your property.</p>
    </div>
    <div class="addon" style="left:355px;top:138px;width:137px;min-height:275px">
      <div class="pkg-head" style="height:56px;padding-bottom:18px">ENHANCED PROPERTY LINES</div>
      <div class="price" style="top:34px">$30</div>
      <p class="body" style="margin-top:50px">Property lines may be added to one of your aerial images and any full-motion video footage or can be applied to three still images from your shoot with unique vantage points. You choose! This is the ideal way to show off unique locations, vacant land and property with lots and acreage.<br>We limit property lines to one parcel per order.</p>
      <p class="body" style="margin-top:7px">Additional property lines may be added at $30 per additional parcel. Home Lens Studio Extra aerial views with property lines DO NOT establish actual property lines and can not be used for legal surveying needs.</p>
    </div>
    <div class="addon" style="left:355px;top:432px;width:137px;min-height:128px">
      <div class="pkg-head" style="height:56px;padding-bottom:18px">VIRTUAL RENOVATIONS</div>
      <div class="price" style="top:34px">$30</div>
      <p class="body" style="margin-top:50px">Let us remove unwanted items from your photos to create the best representation of your property.</p>
    </div>
    <div class="addon" style="left:355px;top:582px;width:137px;min-height:128px">
      <div class="pkg-head" style="height:56px;padding-bottom:18px">VIRTUAL STAGING –<br>360-DEGREE</div>
      <div class="price" style="top:34px">$40</div>
      <p class="body" style="margin-top:50px">Let us make sure your vacant property comes to life with virtual staging!</p>
    </div>
    <div class="addon" style="left:355px;top:730px;width:137px;min-height:128px">
      <div class="pkg-head" style="height:56px;padding-bottom:18px">VIRTUAL RENOVATIONS –<br>360-DEGREE</div>
      <div class="price" style="top:34px">$30</div>
      <p class="body" style="margin-top:50px">Let us remove unwanted items from your photos to create the best</p>
    </div>
  </section>

  <section class="abs" style="top:1720px;left:0;width:537px;height:300px;background:linear-gradient(160deg,#fff,#f6f6f6)">
    <h2 class="abs" style="left:0;width:537px;text-align:center;top:54px;font-size:13px;font-weight:900;color:var(--ink)">GET IN <span style="color:var(--red)">TOUCH WITH</span> US</h2>
    <div class="abs" style="left:50px;top:103px;font-size:11px;font-weight:700;color:var(--ink)">Address</div>
    <div class="c-item" style="left:51px;top:122px"><div class="c-icon"><svg viewBox="0 0 10 10"><path d="M5 0a3.5 3.5 0 0 0-3.5 3.5C1.5 6 5 10 5 10s3.5-4 3.5-6.5A3.5 3.5 0 0 0 5 0zm0 5a1.4 1.4 0 1 1 0-2.8A1.4 1.4 0 0 1 5 5z"/></svg></div><div><h4>LOCATION</h4><p>Marla Whitcombe Real Estate<br>Photographer. United States</p></div></div>
    <div class="c-item" style="left:51px;top:166px"><div class="c-icon"><svg viewBox="0 0 10 10"><path d="M2 0l2 2-1 1.5c.6 1.3 2 2.7 3.5 3.5L8 6l2 2-1.5 2C4 10 0 6 0 1.5z"/></svg></div><div><h4>PHONE NUMBER</h4><p>+1 555 010 8888</p></div></div>
    <div class="c-item" style="left:51px;top:210px"><div class="c-icon"><svg viewBox="0 0 10 10"><path d="M0 2h10v6H0z"/><path d="M0 2l5 3.5L10 2" stroke="#15948f" stroke-width=".8" fill="none"/></svg></div><div><h4>EMAIL ADDRESS</h4><p>info@marlawhitcombe.example</p></div></div>
    <div class="form" style="left:249px;top:92px;width:238px;height:179px">
      <div class="row"><div class="field">First Name</div><div class="field">Your Email</div></div>
      <div class="row"><div class="field">Your Phone</div><div class="field">Address</div></div>
      <div class="field msg">Message</div>
      <span class="btn btn--teal" style="width:62px;line-height:19px;margin-left:3px"><b>SUBMIT</b></span>
    </div>
    <div class="dots" style="left:465px;top:237px"></div>
  </section>

  <footer class="footer" style="top:2017px;height:174px;background:transparent">
    <svg class="abs" style="left:0;top:0" width="537" height="174" viewBox="0 0 537 174">
      <polygon points="0,40 268,2 537,40 537,174 0,174" fill="var(--red)"/>
      <polygon points="0,52 268,14 537,52 537,174 0,174" fill="#fff"/>
      <polygon points="0,62 268,24 537,62 537,174 0,174" fill="var(--black)"/>
    </svg>
    <div class="brand" style="left:49px;top:94px;flex-direction:column;align-items:flex-start;gap:3px">
      <span style="display:flex;align-items:center;gap:5px;color:var(--red);font-size:12px"><i style="width:10px;height:10px;background:var(--red);border-radius:0"></i>Marla Whitcombe</span>
      <span style="font-family:Lato,sans-serif;font-size:7px;color:var(--teal);font-weight:700;padding-left:15px">Real Estate Photographer</span>
    </div>
    <nav class="f-nav" style="left:216px;top:97px"><span>HOME</span><span>ABOUT</span><span>REAL ESTATE</span><span>SPORTS</span><span>DIGITAL TRANSFERS</span><span>CONTACT US</span></nav>
    <div class="f-line" style="left:216px;top:115px">Phone : +1 555 010 8888 &nbsp;&nbsp; | &nbsp;&nbsp; Email : info@marlawhitcombe.example</div>
    <div class="f-line" style="left:216px;top:132px">Copyrights@2023.Marla Whitcombe Real Estate Photographer.All Rights Reserved</div>
    <div class="socials" style="left:216px;top:149px"><i></i><i></i><i></i><i></i></div>
    <div class="f-bar"></div>
  </footer>
</main>

</body>
</html>
```